Tolvane Consulting Powerpoint Template

I require a powerpoint template that I can use for presentations and for report writing. Template should include:
* Cover page with company logo and space for presentation title, and client logo if required.
* Proposed font and heading styles to match the logo (demonstrated through some sample text)
* Three different examples of presentation pages that can be tailored to different clients
* End page for contact details of the presenter or other report details. (so template should be five pages in total length)

The overall style of the template is professional, but with an eye-catching style.

Target Market(s)

Government clients

Industry/Entity Type

Government

Requirements
Must have
• Three different presentation pages that can be optional.
• Proposed font / heading styles for presentation with sample texts
• Use colour pallet: http://www.huemixer.example/palette/417639/Quiet_Harbor
• Clear, crisp and professional design.
Should not have
• Pictures

```html
<!DOCTYPE html>
<html lang="en">
<head>
<meta charset="utf-8">
<title>Tolvane Consulting – Presentation Template</title>
<link href="https://fonts.googleapis.com/css2?family=Raleway:wght@300;400;600&display=swap" rel="stylesheet">
<style>
:root{
  --navy:#262f48;
  --tan:#d4b598;
  --sage:#a6aea6;
  --charcoal:#3b3b3d;
  --ink:#4a4f5c;
  --mute:#9a9ca3;
  --line:#e3e3e6;
  --paper:#ffffff;
  --soft:#c9ccd4;
  --bg:#eef0f2;
}
*{box-sizing:border-box;margin:0;padding:0}
html,body{width:1200px;height:3148px;overflow:hidden;background:var(--bg)}
body{font-family:'Raleway',Arial,sans-serif;color:var(--ink)}
.sheet{width:1200px;height:3148px;padding-top:1px;display:grid;grid-template-columns:repeat(3,394px);column-gap:9px;row-gap:5px;grid-auto-rows:220px}
.slide{position:relative;overflow:hidden;background:var(--paper)}
.abs{position:absolute}
.dark{background:var(--navy);color:#fff}
.title{position:absolute;left:12px;top:9px;font-weight:300;font-size:12px;letter-spacing:.5px;text-transform:uppercase;color:var(--navy)}
.hero{font-weight:300;font-size:15px;letter-spacing:.5px;text-transform:uppercase;color:var(--navy);white-space:nowrap}
.sub{font-size:5.5px;color:var(--mute);white-space:nowrap}
.p{font-size:4.6px;line-height:1.45;color:var(--mute)}
.h{font-size:6px;font-weight:600;color:var(--ink)}
.on-dark,.dark .title{color:#fff}
.tan{background:var(--tan)}.sage{background:var(--sage)}.navy{background:var(--navy)}.char{background:var(--charcoal)}
.brand{position:absolute;display:flex;flex-direction:column;align-items:center;gap:3px}
.brand .mark{width:13px;height:13px;border-radius:50%;background:var(--tan)}
.brand .name{font-size:6.5px;letter-spacing:2.5px;font-weight:400;color:var(--ink);text-transform:uppercase;text-align:center;line-height:1.2}
.client{position:absolute;display:flex;flex-direction:column;align-items:center;gap:3px}
.client .mark{width:13px;height:13px;border:1px solid var(--ink);border-radius:50%}
.client .name{font-size:5px;color:var(--ink)}
.divider-v{position:absolute;width:1px;background:var(--line)}
.foot{position:absolute;left:12px;right:12px;bottom:5px;height:12px;display:flex;align-items:center;justify-content:space-between;border-top:1px solid var(--line);font-size:4px;color:var(--mute)}
.foot .fmark{width:7px;height:7px;border-radius:50%;border:1px solid var(--mute)}
.badge{display:inline-flex;align-items:center;justify-content:center;border-radius:50%;flex:none}
.badge.ring{border:1px solid currentColor}
.ico{width:60%;height:60%;fill:none;stroke:currentColor;stroke-width:1.8;stroke-linecap:round;stroke-linejoin:round}
.num{display:inline-flex;align-items:center;justify-content:center;width:16px;height:9px;background:var(--navy);color:#fff;font-size:5px;flex:none}
.ph{position:absolute}
.row{display:flex}
</style>
</head>
<body>
<svg width="0" height="0" style="position:absolute" aria-hidden="true">
  <defs>
    <symbol id="i-tick" viewBox="0 0 24 24"><polyline points="5,12 10,17 19,7"/></symbol>
    <symbol id="i-arrow" viewBox="0 0 24 24"><line x1="5" y1="12" x2="19" y2="12"/><polyline points="13,6 19,12 13,18"/></symbol>
    <symbol id="i-pin" viewBox="0 0 24 24"><path d="M12 21s-6-6.5-6-11a6 6 0 0 1 12 0c0 4.5-6 11-6 11z"/><circle cx="12" cy="10" r="2.2"/></symbol>
    <symbol id="i-phone" viewBox="0 0 24 24"><rect x="7" y="3" width="10" height="18" rx="2"/><line x1="11" y1="18" x2="13" y2="18"/></symbol>
    <symbol id="i-mail" viewBox="0 0 24 24"><rect x="3" y="6" width="18" height="12"/><polyline points="3,6 12,13 21,6"/></symbol>
    <symbol id="i-search" viewBox="0 0 24 24"><circle cx="10" cy="10" r="6"/><line x1="15" y1="15" x2="20" y2="20"/></symbol>
    <symbol id="i-bulb" viewBox="0 0 24 24"><path d="M9 16c0-2-3-3.5-3-7a6 6 0 0 1 12 0c0 3.5-3 5-3 7z"/><line x1="9.5" y1="19" x2="14.5" y2="19"/><line x1="10.5" y1="21.5" x2="13.5" y2="21.5"/></symbol>
    <symbol id="i-chart" viewBox="0 0 24 24"><line x1="4" y1="20" x2="20" y2="20"/><rect x="6" y="12" width="3" height="8"/><rect x="11" y="7" width="3" height="13"/><rect x="16" y="10" width="3" height="10"/></symbol>
    <symbol id="i-star" viewBox="0 0 24 24"><polygon points="12,3 14.6,9 21,9.5 16,13.8 17.6,20.5 12,17 6.4,20.5 8,13.8 3,9.5 9.4,9"/></symbol>
    <symbol id="i-clock" viewBox="0 0 24 24"><circle cx="12" cy="12" r="8.5"/><polyline points="12,7 12,12 15.5,14"/></symbol>
    <symbol id="i-target" viewBox="0 0 24 24"><circle cx="12" cy="12" r="8.5"/><circle cx="12" cy="12" r="4.5"/><circle cx="12" cy="12" r="1"/></symbol>
    <symbol id="i-gear" viewBox="0 0 24 24"><circle cx="12" cy="12" r="3.5"/><path d="M12 3v3M12 18v3M3 12h3M18 12h3M5.6 5.6l2.1 2.1M16.3 16.3l2.1 2.1M5.6 18.4l2.1-2.1M16.3 7.7l2.1-2.1"/></symbol>
    <symbol id="i-chat" viewBox="0 0 24 24"><path d="M4 5h16v11H10l-4 4v-4H4z"/></symbol>
    <symbol id="i-heart" viewBox="0 0 24 24"><path d="M12 20s-7-4.5-7-10a4 4 0 0 1 7-2.5A4 4 0 0 1 19 10c0 5.5-7 10-7 10z"/></symbol>
  </defs>
</svg>
<main class="sheet">

<!-- 1 Cover -->
<section class="slide">
  <div class="brand" style="left:0;right:0;top:72px"><span class="mark" style="width:20px;height:20px"></span><span class="name" style="font-size:9px;letter-spacing:4px">Tolvane<br>Consulting</span></div>
</section>

<!-- 2 Navy cover -->
<section class="slide dark">
  <div class="abs" style="left:-40px;top:55px;width:170px;height:170px;border-radius:50%;background:var(--paper)"></div>
  <div class="abs" style="left:-30px;top:65px;width:150px;height:150px;border-radius:50%;background:var(--sage)"></div>
  <div class="abs" style="left:-5px;top:90px;width:100px;height:100px;border-radius:50%;background:var(--tan)"></div>
  <div class="abs hero on-dark" style="right:12px;top:16px">Your Title Goes Here</div>
  <div class="abs sub" style="right:12px;top:36px;color:var(--soft)">Your Suitable Goes Here</div>
  <div class="abs sub" style="right:12px;bottom:12px;color:var(--soft)">Client Date</div>
</section>

<!-- 3 -->
<section class="slide">
  <div class="abs tan" style="left:0;top:36px;width:120px;height:12px"></div>
  <div class="brand" style="left:210px;top:28px"><span class="mark"></span><span class="name">Tolvane<br>Consulting</span></div>
  <div class="divider-v" style="left:290px;top:30px;height:34px"></div>
  <div class="client" style="left:305px;top:28px"><span class="mark"></span><span class="name">Harbor Labels</span></div>
  <div class="abs hero" style="right:12px;top:148px">Your Title Goes Here</div>
  <div class="abs sub" style="right:12px;top:168px">Your Suitable Goes Here</div>
</section>

<!-- 4 -->
<section class="slide">
  <div class="abs sage" style="left:0;top:82px;width:130px;height:12px"></div>
  <div class="brand" style="left:150px;top:40px"><span class="mark"></span><span class="name">Tolvane<br>Consulting</span></div>
  <div class="divider-v" style="left:232px;top:42px;height:34px"></div>
  <div class="client" style="left:248px;top:40px"><span class="mark"></span><span class="name">Harbor Labels</span></div>
  <div class="abs hero" style="left:110px;top:144px">Your Title Goes Here</div>
  <div class="abs sub" style="left:210px;top:164px">Your Suitable Goes Here</div>
</section>

<!-- 5 -->
<section class="slide">
  <div class="abs navy" style="left:0;top:82px;width:130px;height:12px"></div>
  <div class="brand" style="left:150px;top:40px"><span class="mark"></span><span class="name">Tolvane<br>Consulting</span></div>
  <div class="divider-v" style="left:232px;top:42px;height:34px"></div>
  <div class="client" style="left:248px;top:40px"><span class="mark"></span><span class="name">Harbor Labels</span></div>
  <div class="abs hero" style="left:110px;top:144px">Your Title Goes Here</div>
  <div class="abs sub" style="left:210px;top:164px">Your Suitable Goes Here</div>
</section>

<!-- 6 -->
<section class="slide">
  <div class="brand" style="left:100px;top:40px"><span class="mark"></span><span class="name">Tolvane<br>Consulting</span></div>
  <div class="divider-v" style="left:184px;top:42px;height:34px"></div>
  <div class="client" style="left:200px;top:40px"><span class="mark"></span><span class="name">Harbor Labels</span></div>
  <div class="abs hero" style="left:60px;top:150px">Your Title Goes Here</div>
  <div class="abs" style="left:40px;right:0;top:172px;height:1px;background:var(--line)"></div>
  <div class="abs sub" style="left:160px;top:178px">Your Suitable Goes Here</div>
</section>

<!-- 7 -->
<section class="slide">
  <div class="brand" style="left:100px;top:60px"><span class="mark"></span><span class="name">Tolvane<br>Consulting</span></div>
  <div class="divider-v" style="left:184px;top:62px;height:34px"></div>
  <div class="client" style="left:200px;top:60px"><span class="mark"></span><span class="name">Harbor Labels</span></div>
  <div class="abs" style="left:0;right:0;top:138px;height:2px;background:var(--tan)"></div>
  <div class="abs hero" style="left:0;right:0;top:168px;text-align:center">Your Title Goes Here</div>
</section>

<!-- 8 -->
<section class="slide">
  <div class="brand" style="left:100px;top:60px"><span class="mark"></span><span class="name">Tolvane<br>Consulting</span></div>
  <div class="divider-v" style="left:184px;top:62px;height:34px"></div>
  <div class="client" style="left:200px;top:60px"><span class="mark"></span><span class="name">Harbor Labels</span></div>
  <div class="abs" style="left:0;right:0;top:138px;height:2px;background:var(--navy)"></div>
  <div class="abs hero" style="left:0;right:0;top:168px;text-align:center">Your Title Goes Here</div>
</section>

<!-- 9 -->
<section class="slide">
  <svg class="abs" width="394" height="220" viewBox="0 0 394 220"><polygon points="0,0 394,0 394,150 300,220 0,220" fill="var(--tan)"/><polygon points="0,0 60,0 0,45" fill="var(--paper)"/></svg>
  <div class="abs hero on-dark" style="right:24px;top:92px">Your Title Goes Here</div>
  <div class="abs sub on-dark" style="right:24px;top:112px">Your Suitable Goes Here</div>
  <div class="client" style="right:14px;bottom:8px"><span class="mark"></span></div>
</section>

<!-- 10 -->
<section class="slide">
  <svg class="abs" width="394" height="220" viewBox="0 0 394 220"><polygon points="60,0 394,0 394,150 300,220 0,220 0,45" fill="var(--sage)"/></svg>
  <div class="abs hero on-dark" style="left:80px;top:92px">Your Title Goes Here</div>
  <div class="abs sub on-dark" style="right:60px;top:114px">Your Suitable Goes Here</div>
  <div class="client" style="right:14px;bottom:8px"><span class="mark"></span></div>
</section>

<!-- 11 -->
<section class="slide">
  <svg class="abs" width="394" height="220" viewBox="0 0 394 220"><polygon points="60,0 394,0 394,150 300,220 0,220 0,45" fill="var(--navy)"/></svg>
  <div class="abs hero on-dark" style="left:80px;top:92px">Your Title Goes Here</div>
  <div class="abs sub on-dark" style="right:60px;top:114px">Your Suitable Goes Here</div>
  <div class="client" style="right:14px;bottom:8px"><span class="mark"></span></div>
</section>

<!-- 12 Agenda -->
<section class="slide">
  <div class="title">Our Agenda</div>
  <div class="abs" style="left:14px;top:48px;display:grid;grid-template-columns:180px 180px;row-gap:22px">
    <div class="row" style="gap:6px"><span class="num">01</span><div><div class="h">Agenda One</div><div class="p">Short notes for this point.</div></div></div>
    <div class="row" style="gap:6px"><span class="num">04</span><div><div class="h">Agenda Four</div><div class="p">Short notes for this point.</div></div></div>
    <div class="row" style="gap:6px"><span class="num">02</span><div><div class="h">Agenda Two</div><div class="p">Short notes for this point.</div></div></div>
    <div class="row" style="gap:6px"><span class="num">05</span><div><div class="h">Agenda Five</div><div class="p">Short notes for this point.</div></div></div>
    <div class="row" style="gap:6px"><span class="num">03</span><div><div class="h">Agenda Three</div><div class="p">Short notes for this point.</div></div></div>
    <div class="row" style="gap:6px"><span class="num">06</span><div><div class="h">Agenda Six</div><div class="p">Short notes for this point.</div></div></div>
  </div>
  <div class="foot"><span>Tolvane Consulting · Presentation Title</span><span class="fmark"></span></div>
</section>

<!-- 13 Four columns -->
<section class="slide">
  <div class="title">Your Title Here</div>
  <div class="abs row" style="left:0;right:0;top:40px;height:150px">
    <div class="tan" style="flex:1;padding:14px 8px;text-align:center;color:#fff"><span class="badge" style="width:16px;height:16px;color:#fff"><svg class="ico" style="width:100%;height:100%"><use href="#i-gear"/></svg></span><div class="h" style="color:#fff;margin-top:12px">Experience</div><p class="p" style="color:#fff">Short text describes this item in two lines.</p></div>
    <div style="flex:1;padding:14px 8px;text-align:center;color:#fff;background:#cdae91"><span class="badge" style="width:16px;height:16px;color:#fff"><svg class="ico" style="width:100%;height:100%"><use href="#i-bulb"/></svg></span><div class="h" style="color:#fff;margin-top:12px">Creative Idea</div><p class="p" style="color:#fff">Short text describes this item in two lines.</p></div>
    <div class="navy" style="flex:1;padding:14px 8px;text-align:center;color:#fff"><span class="badge" style="width:16px;height:16px;color:#fff"><svg class="ico" style="width:100%;height:100%"><use href="#i-chart"/></svg></span><div class="h" style="color:#fff;margin-top:12px">Strategy</div><p class="p" style="color:var(--soft)">Short text describes this item in two lines.</p></div>
    <div class="char" style="flex:1;padding:14px 8px;text-align:center;color:#fff"><span class="badge" style="width:16px;height:16px;color:#fff"><svg class="ico" style="width:100%;height:100%"><use href="#i-chat"/></svg></span><div class="h" style="color:#fff;margin-top:12px">Support</div><p class="p" style="color:#ddd">Short text describes this item in two lines.</p></div>
  </div>
  <div class="foot"><span>Tolvane Consulting · Presentation Title</span><span class="fmark"></span></div>
</section>

<!-- 14 Divider -->
<section class="slide">
  <div class="brand" style="left:255px;top:60px"><span class="mark"></span></div>
  <div class="abs hero" style="left:200px;top:86px">Divider Page</div>
  <div class="abs sub" style="left:232px;top:106px">Your Suitable Here</div>
  <div class="foot"><span>Tolvane Consulting · Presentation Title</span><span class="fmark"></span></div>
</section>

<!-- 15 Text & bullets -->
<section class="slide">
  <div class="title">Text &amp; Bullet Area</div>
  <div class="abs" style="left:12px;top:40px;width:150px"><div class="h">Heading Goes Here</div><p class="p" style="margin-top:6px">Use this space for a clear paragraph that explains the key idea of the page in simple terms for every reader.</p><p class="p" style="margin-top:6px">A second paragraph adds detail, figures or a short summary of the next steps for the team.</p></div>
  <div class="abs" style="left:180px;top:40px;display:grid;grid-template-columns:100px 100px;row-gap:14px">
    <div class="row" style="gap:5px"><span class="badge tan" style="width:14px;height:14px;color:#fff"><svg class="ico"><use href="#i-star"/></svg></span><div><div class="h" style="color:var(--tan)">Your Text Here</div><div class="p">Short line of text.</div></div></div>
    <div class="row" style="gap:5px"><span class="badge sage" style="width:14px;height:14px;color:#fff"><svg class="ico"><use href="#i-tick"/></svg></span><div><div class="h">Your Text Here</div><div class="p">Short line of text.</div></div></div>
    <div class="row" style="gap:5px"><span class="badge tan" style="width:14px;height:14px;color:#fff"><svg class="ico"><use href="#i-clock"/></svg></span><div><div class="h" style="color:var(--tan)">Your Text Here</div><div class="p">Short line of text.</div></div></div>
    <div class="row" style="gap:5px"><span class="badge navy" style="width:14px;height:14px;color:#fff"><svg class="ico"><use href="#i-target"/></svg></span><div><div class="h">Your Text Here</div><div class="p">Short line of text.</div></div></div>
    <div class="row" style="gap:5px"><span class="badge tan" style="width:14px;height:14px;color:#fff"><svg class="ico"><use href="#i-heart"/></svg></span><div><div class="h" style="color:var(--tan)">Your Text Here</div><div class="p">Short line of text.</div></div></div>
    <div class="row" style="gap:5px"><span class="badge sage" style="width:14px;height:14px;color:#fff"><svg class="ico"><use href="#i-chat"/></svg></span><div><div class="h">Your Text Here</div><div class="p">Short line of text.</div></div></div>
  </div>
  <div class="foot"><span>Tolvane Consulting · Presentation Title</span><span class="fmark"></span></div>
</section>

<!-- 16 Five columns -->
<section class="slide">
  <div class="abs row" style="inset:0">
    <div class="tan" style="flex:1;padding:30px 8px;text-align:center;border-right:1px solid #fff"><span class="badge" style="width:18px;height:18px;color:#fff"><svg class="ico" style="width:100%;height:100%"><use href="#i-gear"/></svg></span><p class="p" style="color:#fff;margin-top:30px">Your short text for this column goes here.</p></div>
    <div class="tan" style="flex:1;padding:30px 8px;text-align:center;border-right:1px solid #fff"><span class="badge" style="width:18px;height:18px;color:#fff"><svg class="ico" style="width:100%;height:100%"><use href="#i-chart"/></svg></span><p class="p" style="color:#fff;margin-top:30px">Your short text for this column goes here.</p></div>
    <div class="tan" style="flex:1;padding:30px 8px;text-align:center;border-right:1px solid #fff"><span class="badge" style="width:18px;height:18px;color:#fff"><svg class="ico" style="width:100%;height:100%"><use href="#i-search"/></svg></span><p class="p" style="color:#fff;margin-top:30px">Your short text for this column goes here.</p></div>
    <div class="tan" style="flex:1;padding:30px 8px;text-align:center;border-right:1px solid #fff"><span class="badge" style="width:18px;height:18px;color:#fff"><svg class="ico" style="width:100%;height:100%"><use href="#i-target"/></svg></span><p class="p" style="color:#fff;margin-top:30px">Your short text for this column goes here.</p></div>
    <div class="sage" style="flex:1;padding:30px 8px;text-align:center"><span class="badge" style="width:18px;height:18px;color:#fff"><svg class="ico" style="width:100%;height:100%"><use href="#i-star"/></svg></span><p class="p" style="color:#fff;margin-top:30px">Your short text for this column goes here.</p></div>
  </div>
</section>

<!-- 17 Mockup area -->
<section class="slide">
  <div class="title">Our Mockup Area</div>
  <div class="abs navy" style="left:0;right:0;top:150px;height:70px"></div>
  <div class="ph" role="img" aria-label="Laptop mockup showing the Tolvane Consulting title screen" style="left:115px;top:30px;width:170px;height:120px;background:linear-gradient(#e9eaec,#c9ccd1);border-radius:4px"></div>
  <div class="abs tan" style="left:12px;top:56px;width:30px;height:8px"></div>
  <div class="abs navy" style="left:12px;top:72px;width:30px;height:8px"></div>
  <div class="abs tan" style="left:12px;top:110px;width:30px;height:8px"></div>
  <div class="abs tan" style="right:12px;top:56px;width:30px;height:8px"></div>
  <div class="abs navy" style="right:12px;top:80px;width:30px;height:8px"></div>
  <div class="abs navy" style="right:12px;top:104px;width:30px;height:8px"></div>
  <svg class="abs" width="394" height="220" style="left:0;top:0"><g stroke="var(--ink)" stroke-width=".5"><line x1="42" y1="60" x2="130" y2="60"/><line x1="42" y1="76" x2="130" y2="90"/><line x1="42" y1="114" x2="130" y2="114"/><line x1="270" y1="60" x2="352" y2="60"/><line x1="270" y1="90" x2="352" y2="84"/><line x1="270" y1="108" x2="352" y2="108"/></g></svg>
</section>

<!-- 18 Picture + bars -->
<section class="slide">
  <div class="abs navy" style="left:0;top:0;width:150px;height:220px"></div>
  <div class="abs" style="left:30px;top:38px;width:70px;height:70px;border:1px solid #fff;border-radius:50%;display:flex;align-items:center;justify-content:center;text-align:center;font-size:7px;font-weight:300;color:#fff;line-height:1.3">RIGHT<br>PICTURE<br>SLIDE</div>
  <p class="p abs" style="left:24px;top:118px;width:90px;color:var(--soft)">Short description sits beneath the circle here.</p>
  <svg class="abs" style="left:190px;top:25px" width="190" height="120" viewBox="0 0 190 120"><rect x="8" y="50" width="8" height="70" fill="var(--tan)"/><rect x="20" y="30" width="8" height="90" fill="var(--charcoal)"/><rect x="44" y="60" width="8" height="60" fill="var(--tan)"/><rect x="56" y="40" width="8" height="80" fill="var(--sage)"/><rect x="80" y="70" width="8" height="50" fill="var(--tan)"/><rect x="92" y="35" width="8" height="85" fill="var(--charcoal)"/><rect x="116" y="45" width="8" height="75" fill="var(--tan)"/><rect x="128" y="20" width="8" height="100" fill="var(--sage)"/><rect x="152" y="30" width="8" height="90" fill="var(--tan)"/><rect x="164" y="5" width="8" height="115" fill="var(--charcoal)"/></svg>
  <svg class="abs" style="left:186px;top:162px" width="10" height="10"><polygon points="5,1 9,9 1,9" fill="var(--tan)"/></svg>
  <div class="abs" style="left:200px;top:156px;font-size:15px;font-weight:300;color:var(--ink)">85%</div>
  <div class="foot" style="left:160px"><span>Presentation Title</span><span class="fmark"></span></div>
</section>

<!-- 19 Our mockup -->
<section class="slide">
  <div class="abs navy" style="left:0;right:0;top:0;height:70px"></div>
  <div class="title on-dark">Our Mockup</div>
  <div class="abs sub" style="left:12px;top:26px;color:var(--soft)">Heading Here</div>
  <p class="p abs" style="left:12px;top:36px;width:150px;color:var(--soft)">Introduce the mockup with a short and clear line of supporting text.</p>
  <div class="ph" role="img" aria-label="Desktop monitor mockup showing the Tolvane Consulting title screen" style="left:180px;top:24px;width:150px;height:110px;background:linear-gradient(#f2f3f4,#c5c8cd);border-radius:3px"></div>
  <div class="abs" style="left:12px;top:96px;width:150px">
    <div class="row" style="gap:5px;margin-bottom:10px"><span class="badge tan" style="width:9px;height:9px;color:#fff"><svg class="ico"><use href="#i-tick"/></svg></span><p class="p">Point one explained in a short sentence here.</p></div>
    <div class="row" style="gap:5px;margin-bottom:10px"><span class="badge sage" style="width:9px;height:9px;color:#fff"><svg class="ico"><use href="#i-tick"/></svg></span><p class="p">Point two explained in a short sentence here.</p></div>
    <div class="row" style="gap:5px"><span class="badge tan" style="width:9px;height:9px;color:#fff"><svg class="ico"><use href="#i-tick"/></svg></span><p class="p">Point three explained in a short sentence here.</p></div>
  </div>
  <div class="foot"><span>Tolvane Consulting · Presentation Title</span><span class="fmark"></span></div>
</section>

<!-- 20 Line chart -->
<section class="slide">
  <div class="abs hero" style="left:12px;top:20px;font-size:11px;line-height:1.2">This is Line<br>Chart Slide</div>
  <div class="abs navy" style="left:12px;top:54px;padding:2px 6px;font-size:5px;color:#fff">Heading Text Here</div>
  <p class="p abs" style="left:12px;top:72px;width:100px">Describe the trend shown in the chart in one or two short lines.</p>
  <svg class="abs" style="left:140px;top:30px" width="240" height="150" viewBox="0 0 240 150"><g stroke="var(--line)" stroke-width=".5"><line x1="10" y1="20" x2="230" y2="20"/><line x1="10" y1="60" x2="230" y2="60"/><line x1="10" y1="100" x2="230" y2="100"/><line x1="10" y1="140" x2="230" y2="140"/></g><polyline points="20,40 90,110 160,50 225,120" fill="none" stroke="var(--tan)" stroke-width="1.2"/><polyline points="20,90 90,30 160,100 225,70" fill="none" stroke="var(--sage)" stroke-width="1.2"/></svg>
  <div class="foot"><span>Tolvane Consulting · Presentation Title</span><span class="fmark"></span></div>
</section>

<!-- 21 Navy divider -->
<section class="slide">
  <svg class="abs" width="394" height="220" viewBox="0 0 394 220"><polygon points="0,0 394,0 394,150 310,220 0,220" fill="var(--navy)"/></svg>
  <div class="abs hero on-dark" style="left:0;right:0;top:92px;text-align:center">This is Your Divider Page</div>
  <div class="abs sub" style="right:90px;top:112px;color:var(--soft)">Your Suitable Goes Here</div>
  <div class="brand" style="right:12px;bottom:6px"><span class="mark" style="width:8px;height:8px"></span><span class="name" style="font-size:4px">Tolvane Consulting</span></div>
</section>

<!-- 22 Product philosophy -->
<section class="slide">
  <div class="title">Product Philosophy</div>
  <svg class="abs" style="left:147px;top:38px" width="100" height="100" viewBox="0 0 100 100"><g fill="none" stroke-width="22" transform="rotate(-90 50 50)"><circle cx="50" cy="50" r="36" stroke="var(--tan)" stroke-dasharray="90 226"/><circle cx="50" cy="50" r="36" stroke="var(--navy)" stroke-dasharray="55 226" stroke-dashoffset="-90"/><circle cx="50" cy="50" r="36" stroke="var(--sage)" stroke-dasharray="45 226" stroke-dashoffset="-145"/><circle cx="50" cy="50" r="36" stroke="var(--charcoal)" stroke-dasharray="36 226" stroke-dashoffset="-190"/></g></svg>
  <div class="abs row" style="left:30px;top:50px;width:112px;gap:5px;justify-content:flex-end"><div style="text-align:right"><div class="h" style="color:var(--tan)">Quality</div><p class="p">Short text about this value.</p></div><span class="badge ring" style="width:13px;height:13px;color:var(--tan)"><svg class="ico"><use href="#i-star"/></svg></span></div>
  <div class="abs row" style="left:30px;top:120px;width:112px;gap:5px;justify-content:flex-end"><div style="text-align:right"><div class="h">Loyalty</div><p class="p">Short text about this value.</p></div><span class="badge ring" style="width:13px;height:13px;color:var(--ink)"><svg class="ico"><use href="#i-heart"/></svg></span></div>
  <div class="abs row" style="left:252px;top:50px;width:120px;gap:5px"><span class="badge ring" style="width:13px;height:13px;color:var(--ink)"><svg class="ico"><use href="#i-chart"/></svg></span><div><div class="h">Performance</div><p class="p">Short text about this value.</p></div></div>
  <div class="abs row" style="left:252px;top:120px;width:120px;gap:5px"><span class="badge ring" style="width:13px;height:13px;color:var(--ink)"><svg class="ico"><use href="#i-bulb"/></svg></span><div><div class="h">Innovation</div><p class="p">Short text about this value.</p></div></div>
  <div class="foot"><span>Tolvane Consulting · Presentation Title</span><span class="fmark"></span></div>
</section>

<!-- 23 Bar chart -->
<section class="slide">
  <div class="abs navy" style="left:0;right:0;top:150px;height:70px"></div>
  <div class="abs sub" style="left:0;right:0;top:10px;text-align:center">Annual Review</div>
  <svg class="abs" style="left:20px;top:30px" width="354" height="120" viewBox="0 0 354 120"><rect x="10" y="50" width="14" height="70" fill="var(--tan)"/><rect x="28" y="30" width="14" height="90" fill="var(--sage)"/><rect x="80" y="60" width="14" height="60" fill="var(--tan)"/><rect x="98" y="5" width="14" height="115" fill="var(--tan)"/><rect x="150" y="40" width="14" height="80" fill="var(--sage)"/><rect x="200" y="70" width="14" height="50" fill="var(--tan)"/><rect x="218" y="80" width="14" height="40" fill="var(--sage)"/><rect x="270" y="85" width="14" height="35" fill="var(--tan)"/><rect x="288" y="95" width="14" height="25" fill="var(--sage)"/></svg>
  <div class="abs row" style="left:20px;right:20px;top:160px;gap:10px">
    <div style="flex:1"><div class="h" style="color:#fff">Plan</div><p class="p" style="color:var(--soft)">Short note for this year.</p></div>
    <div style="flex:1"><div class="h" style="color:#fff">Grow</div><p class="p" style="color:var(--soft)">Short note for this year.</p></div>
    <div style="flex:1"><div class="h" style="color:#fff">Review</div><p class="p" style="color:var(--soft)">Short note for this year.</p></div>
    <div style="flex:1"><div class="h" style="color:#fff">Deliver</div><p class="p" style="color:var(--soft)">Short note for this year.</p></div>
  </div>
</section>

<!-- 24 Trending -->
<section class="slide">
  <div class="title">Trending in the World</div>
  <div class="ph" role="img" aria-label="World map with location markers" style="left:12px;top:34px;width:250px;height:140px;background:linear-gradient(#cfd2d3,#b7bcbc);border-radius:6px"></div>
  <div class="abs" style="left:275px;top:40px;width:110px">
    <div class="row" style="gap:5px;margin-bottom:14px"><span class="badge tan" style="width:12px;height:12px;color:#fff"><svg class="ico"><use href="#i-pin"/></svg></span><div><div class="h">Your Text Here</div><p class="p">Short note.</p></div></div>
    <div class="row" style="gap:5px;margin-bottom:14px"><span class="badge ring" style="width:12px;height:12px;color:var(--ink)"><svg class="ico"><use href="#i-chart"/></svg></span><div><div class="h">Your Text Here</div><p class="p">Short note.</p></div></div>
    <div class="row" style="gap:5px"><span class="badge ring" style="width:12px;height:12px;color:var(--ink)"><svg class="ico"><use href="#i-tick"/></svg></span><div><div class="h">Your Text Here</div><p class="p">Short note.</p></div></div>
  </div>
  <div class="foot"><span>Tolvane Consulting · Presentation Title</span><span class="fmark"></span></div>
</section>

<!-- 25 Three column -->
<section class="slide">
  <div class="title">Three Column Description</div>
  <p class="abs" style="left:12px;top:30px;width:260px;font-size:6.5px;font-weight:300;color:var(--tan)">Use this line to introduce the three topics below and set out the main message.</p>
  <div class="abs row" style="left:12px;right:12px;top:58px;gap:14px">
    <div style="flex:1"><p class="p">First column text gives a short overview of the topic with enough words to fill a few lines of this layout.</p><div class="h" style="margin-top:10px">Sub Heading</div><p class="p">Short supporting line.</p></div>
    <div style="flex:1"><p class="p">Second column text gives a short overview of the topic with enough words to fill a few lines of this layout.</p><div class="h" style="margin-top:10px">Sub Heading</div><p class="p">Short supporting line.</p></div>
    <div style="flex:1"><p class="p">Third column text gives a short overview of the topic with enough words to fill a few lines of this layout.</p><div class="h" style="margin-top:10px">Sub Heading</div><p class="p">Short supporting line.</p></div>
  </div>
  <div class="foot"><span>Tolvane Consulting · Presentation Title</span><span class="fmark"></span></div>
</section>

<!-- 26 Our team -->
<section class="slide">
  <div class="title">Our Team</div>
  <div class="abs" style="left:0;right:0;top:38px;height:1px;background:var(--line)"></div>
  <div class="ph" role="img" aria-label="Portrait photo of a team member" style="left:160px;top:40px;width:72px;height:72px;border-radius:50%;background:linear-gradient(#c9b6a4,#8c8f98)"></div>
  <div class="abs h" style="left:0;right:0;top:118px;text-align:center">Team Member</div>
  <div class="abs sub" style="left:0;right:0;top:127px;text-align:center">CEO</div>
  <p class="p abs" style="left:110px;width:174px;top:138px;text-align:center">Short biography for this person in one or two lines of text.</p>
  <div class="foot"><span>Tolvane Consulting · Presentation Title</span><span class="fmark"></span></div>
</section>

<!-- 27 Clients -->
<section class="slide">
  <div class="abs" role="img" aria-label="Client badge" style="left:24px;top:20px;width:46px;height:22px;background:var(--line)"></div>
  <div class="abs" role="img" aria-label="Client badge" style="left:110px;top:20px;width:40px;height:22px;border-radius:50%;background:var(--line)"></div>
  <div class="abs" role="img" aria-label="Client badge" style="left:210px;top:18px;width:50px;height:26px;background:var(--line)"></div>
  <div class="abs" role="img" aria-label="Client badge" style="left:310px;top:20px;width:50px;height:22px;background:var(--line)"></div>
  <div class="abs navy" style="left:90px;top:80px;width:214px;height:52px;display:flex;align-items:center;justify-content:center;text-align:center;color:#fff;font-weight:300;font-size:12px;line-height:1.15">OUR AWESOME<br>CLIENT</div>
  <div class="abs" role="img" aria-label="Client badge" style="left:24px;top:168px;width:30px;height:30px;border-radius:50%;background:var(--line)"></div>
  <div class="abs" role="img" aria-label="Client badge" style="left:110px;top:168px;width:30px;height:30px;border-radius:50%;background:var(--line)"></div>
  <div class="abs" role="img" aria-label="Client badge" style="left:210px;top:170px;width:50px;height:26px;background:var(--line)"></div>
  <div class="abs" role="img" aria-label="Client badge" style="left:310px;top:168px;width:40px;height:30px;background:var(--line)"></div>
</section>

<!-- 28 Tan divider -->
<section class="slide">
  <svg class="abs" width="394" height="220" viewBox="0 0 394 220"><polygon points="50,0 394,0 394,150 310,220 0,220 0,40" fill="var(--tan)"/></svg>
  <div class="abs hero" style="right:40px;top:120px">This is Your Divider Page</div>
  <div class="abs sub" style="right:90px;top:140px;color:var(--ink)">Your Suitable Goes Here</div>
</section>

<!-- 29 Subscription -->
<section class="slide">
  <div class="title">Monthly Subscription</div>
  <div class="abs navy" style="left:0;right:0;top:42px;height:50px"></div>
  <div class="abs navy" style="left:0;right:0;top:170px;height:50px"></div>
  <div class="abs row" style="left:50px;right:50px;top:60px;gap:10px;align-items:flex-start">
    <div style="flex:1;background:#fff;box-shadow:0 1px 4px rgba(0,0,0,.15)"><div class="char" style="height:28px;color:#fff;font-size:9px;font-weight:300;display:flex;align-items:center;justify-content:center">$100</div><p class="p" style="padding:8px;text-align:center">Basic plan<br>Five users<br>Email support</p></div>
    <div style="flex:1;background:#fff;box-shadow:0 1px 4px rgba(0,0,0,.15);margin-top:-8px"><div class="tan" style="height:36px;color:#fff;font-size:10px;font-weight:300;display:flex;align-items:center;justify-content:center">$200</div><p class="p" style="padding:8px;text-align:center">Standard plan<br>Ten users<br>Phone support</p></div>
    <div style="flex:1;background:#fff;box-shadow:0 1px 4px rgba(0,0,0,.15)"><div class="char" style="height:28px;color:#fff;font-size:9px;font-weight:300;display:flex;align-items:center;justify-content:center">$400</div><p class="p" style="padding:8px;text-align:center">Premium plan<br>All users<br>Full support</p></div>
  </div>
</section>

<!-- 30 Table -->
<section class="slide">
  <div class="title">Your Title Goes Here</div>
  <svg class="abs" style="left:12px;top:32px" width="370" height="160" viewBox="0 0 370 160">
    <rect x="0" y="0" width="370" height="12" fill="var(--navy)"/>
    <g fill="#fff" font-size="5" font-family="Raleway, sans-serif"><text x="110" y="8">Plan A</text><text x="175" y="8">Plan B</text><text x="240" y="8">Plan C</text><text x="305" y="8">Plan D</text></g>
    <g fill="#f3f3f4"><rect y="24" width="370" height="12"/><rect y="48" width="370" height="12"/><rect y="72" width="370" height="12"/><rect y="96" width="370" height="12"/><rect y="120" width="370" height="12"/><rect y="144" width="370" height="12"/></g>
    <g fill="var(--ink)" font-size="4.5" font-family="Raleway, sans-serif"><text x="8" y="20">Feature one</text><text x="8" y="32">Feature two</text><text x="8" y="44">Feature three</text><text x="8" y="56">Feature four</text><text x="8" y="68">Feature five</text><text x="8" y="80">Feature six</text><text x="8" y="92">Feature seven</text><text x="8" y="104">Feature eight</text><text x="8" y="116">Feature nine</text><text x="8" y="128">Feature ten</text><text x="8" y="140">Feature eleven</text><text x="8" y="152">Feature twelve</text></g>
    <g fill="none" stroke="var(--tan)" stroke-width="1" stroke-linecap="round"><polyline points="115,18 117.5,20 121,15.5"/><polyline points="180,30 182.5,32 186,27.5"/><polyline points="245,42 247.5,44 251,39.5"/><polyline points="310,54 312.5,56 316,51.5"/><polyline points="115,66 117.5,68 121,63.5"/><polyline points="180,78 182.5,80 186,75.5"/><polyline points="245,90 247.5,92 251,87.5"/><polyline points="310,102 312.5,104 316,99.5"/><polyline points="115,114 117.5,116 121,111.5"/><polyline points="180,126 182.5,128 186,123.5"/><polyline points="245,138 247.5,140 251,135.5"/><polyline points="310,150 312.5,152 316,147.5"/></g>
  </svg>
  <div class="foot"><span>Tolvane Consulting · Presentation Title</span><span class="fmark"></span></div>
</section>

<!-- 31 Team four -->
<section class="slide">
  <div class="title">Our Team</div>
  <div class="abs" style="left:12px;top:34px;display:grid;grid-template-columns:180px 180px;row-gap:30px">
    <div class="row" style="gap:6px"><div role="img" aria-label="Portrait photo of a team member" style="width:24px;height:24px;border-radius:50%;background:linear-gradient(#c9b6a4,#8c8f98);flex:none"></div><div><div class="h">Team Member</div><div class="sub">Director</div><p class="p">Short biography line here.</p></div></div>
    <div class="row" style="gap:6px"><div role="img" aria-label="Portrait photo of a team member" style="width:24px;height:24px;border-radius:50%;background:linear-gradient(#c9b6a4,#8c8f98);flex:none"></div><div><div class="h">Team Member</div><div class="sub">Manager</div><p class="p">Short biography line here.</p></div></div>
    <div class="row" style="gap:6px"><div role="img" aria-label="Portrait photo of a team member" style="width:24px;height:24px;border-radius:50%;background:linear-gradient(#c9b6a4,#8c8f98);flex:none"></div><div><div class="h">Team Member</div><div class="sub">Consultant</div><p class="p">Short biography line here.</p></div></div>
    <div class="row" style="gap:6px"><div role="img" aria-label="Portrait photo of a team member" style="width:24px;height:24px;border-radius:50%;background:linear-gradient(#c9b6a4,#8c8f98);flex:none"></div><div><div class="h">Team Member</div><div class="sub">Analyst</div><p class="p">Short biography line here.</p></div></div>
  </div>
  <div class="foot"><span>Tolvane Consulting · Presentation Title</span><span class="fmark"></span></div>
</section>

<!-- 32 Maps -->
<section class="slide">
  <div class="abs" style="left:12px;top:18px;font-size:14px;font-weight:400;color:var(--ink);line-height:1.1">Fully<br>Editable<br>Maps.</div>
  <div class="abs" style="left:12px;top:76px;font-size:6.5px;color:var(--tan);line-height:1.3">5 NEW SHOPS<br>THIS YEAR</div>
  <p class="p abs" style="left:12px;top:100px;width:90px">Short note about new locations this year.</p>
  <div class="ph" role="img" aria-label="Regional map with shop location pins" style="left:150px;top:20px;width:190px;height:170px;background:linear-gradient(135deg,var(--sage),var(--tan));border-radius:30px 50px 30px 60px"></div>
  <div class="foot"><span>Tolvane Consulting · Presentation Title</span><span class="fmark"></span></div>
</section>

<!-- 33 Testimonials -->
<section class="slide">
  <div class="title">Customer Testimonials</div>
  <div class="ph" role="img" aria-label="Portrait photo of a customer" style="left:34px;top:34px;width:40px;height:40px;border-radius:50%;background:linear-gradient(#c9b6a4,#8c8f98)"></div>
  <p class="p abs" style="left:90px;top:40px;width:280px">"A short customer quote goes here and tells how the work made a real difference to their team."</p>
  <div class="abs h" style="left:90px;top:62px">Client Name</div>
  <div class="abs navy" style="left:0;right:0;top:108px;height:112px"></div>
  <div class="abs row" style="left:20px;right:20px;top:122px;justify-content:space-around;text-align:center">
    <div><span class="badge ring" style="width:18px;height:18px;color:#fff"><svg class="ico"><use href="#i-star"/></svg></span><p class="p" style="color:var(--soft);margin-top:6px">Short note</p></div>
    <div><span class="badge ring" style="width:18px;height:18px;color:#fff"><svg class="ico"><use href="#i-chat"/></svg></span><p class="p" style="color:var(--soft);margin-top:6px">Short note</p></div>
    <div><span class="badge ring" style="width:18px;height:18px;color:#fff"><svg class="ico"><use href="#i-heart"/></svg></span><p class="p" style="color:var(--soft);margin-top:6px">Short note</p></div>
    <div><span class="badge ring" style="width:18px;height:18px;color:#fff"><svg class="ico"><use href="#i-tick"/></svg></span><p class="p" style="color:var(--soft);margin-top:6px">Short note</p></div>
  </div>
</section>

<!-- 34 Three blocks -->
<section class="slide">
  <div class="abs hero" style="left:0;right:0;top:30px;text-align:center;font-size:12px">Your Title Goes Here</div>
  <div class="abs row" style="left:0;right:0;top:110px;height:68px">
    <div class="tan" style="flex:1;padding:10px"><p class="p" style="color:#fff">Short text block one sits here in two or three lines.</p></div>
    <div class="sage" style="flex:1;padding:10px"><p class="p" style="color:#fff">Short text block two sits here in two or three lines.</p></div>
    <div class="navy" style="flex:1;padding:10px"><p class="p" style="color:var(--soft)">Short text block three sits here in two or three lines.</p></div>
  </div>
  <div class="foot"><span>Tolvane Consulting · Presentation Title</span><span class="fmark"></span></div>
</section>

<!-- 35 Quad -->
<section class="slide">
  <div class="title">Your Title</div>
  <div class="abs sage" style="left:197px;top:0;width:197px;height:110px;padding:14px"><p class="p" style="color:#fff">Text for the top right block goes here with a short idea.</p></div>
  <div class="abs tan" style="left:0;top:110px;width:197px;height:110px;padding:14px"><p class="p" style="color:#fff">Text for the lower left block goes here with a short idea.</p></div>
  <div class="abs row" style="left:12px;top:34px;width:175px;gap:5px"><span class="badge ring" style="width:11px;height:11px;color:var(--tan)"><svg class="ico"><use href="#i-bulb"/></svg></span><div><div class="h" style="color:var(--tan)">Subheading</div><p class="p">Short paragraph text for this section.</p></div></div>
  <div class="abs row" style="left:210px;top:130px;width:175px;gap:5px"><span class="badge ring" style="width:11px;height:11px;color:var(--tan)"><svg class="ico"><use href="#i-target"/></svg></span><div><div class="h" style="color:var(--tan)">Subheading</div><p class="p">Short paragraph text for this section.</p></div></div>
</section>

<!-- 36 Navy column -->
<section class="slide">
  <div class="title">Your Title</div>
  <div class="abs navy" style="left:197px;top:0;width:197px;height:220px;padding:14px"><p class="p" style="color:var(--soft)">Text for the right column goes here with a short idea.</p><p class="p" style="color:var(--soft);margin-top:40px">More text continues here with a second short idea.</p></div>
  <div class="abs sage" style="left:197px;top:92px;width:197px;height:44px"></div>
  <div class="abs" style="left:12px;top:36px;width:170px">
    <div class="row" style="gap:5px;margin-bottom:18px"><span class="badge ring" style="width:11px;height:11px;color:var(--tan)"><svg class="ico"><use href="#i-search"/></svg></span><div><div class="h" style="color:var(--tan)">Bullet One</div><p class="p">Short text here.</p></div></div>
    <div class="row" style="gap:5px;margin-bottom:18px"><span class="badge ring" style="width:11px;height:11px;color:var(--tan)"><svg class="ico"><use href="#i-clock"/></svg></span><div><div class="h" style="color:var(--tan)">Bullet Two</div><p class="p">Short text here.</p></div></div>
    <div class="row" style="gap:5px"><span class="badge ring" style="width:11px;height:11px;color:var(--tan)"><svg class="ico"><use href="#i-arrow"/></svg></span><div><div class="h" style="color:var(--tan)">Bullet Three</div><p class="p">Short text here.</p></div></div>
  </div>
</section>

<!-- 37 Circle infographic -->
<section class="slide">
  <div class="title">Circle Infographic</div>
  <svg class="abs" style="left:137px;top:36px" width="120" height="120" viewBox="0 0 120 120"><g fill="none" stroke-width="28" transform="rotate(-90 60 60)"><circle cx="60" cy="60" r="44" stroke="var(--navy)" stroke-dasharray="67 276"/><circle cx="60" cy="60" r="44" stroke="var(--sage)" stroke-dasharray="67 276" stroke-dashoffset="-69"/><circle cx="60" cy="60" r="44" stroke="var(--navy)" stroke-dasharray="67 276" stroke-dashoffset="-138"/><circle cx="60" cy="60" r="44" stroke="var(--tan)" stroke-dasharray="67 276" stroke-dashoffset="-207"/></g>
    <g fill="none" stroke="#fff" stroke-width="1.8" stroke-linecap="round" stroke-linejoin="round"><use href="#i-gear" x="84" y="22" width="14" height="14"/><use href="#i-chart" x="84" y="84" width="14" height="14"/><use href="#i-target" x="22" y="84" width="14" height="14"/><use href="#i-bulb" x="22" y="22" width="14" height="14"/></g></svg>
  <div class="abs row" style="left:20px;top:50px;width:118px;gap:5px;justify-content:flex-end"><div style="text-align:right"><div class="h" style="color:var(--tan)">Your Text Here</div><p class="p">Short note.</p></div><span class="badge tan" style="width:11px;height:11px;color:#fff;font-size:5px">1</span></div>
  <div class="abs row" style="left:20px;top:120px;width:118px;gap:5px;justify-content:flex-end"><div style="text-align:right"><div class="h" style="color:var(--tan)">Your Text Here</div><p class="p">Short note.</p></div><span class="badge navy" style="width:11px;height:11px;color:#fff;font-size:5px">3</span></div>
  <div class="abs row" style="left:258px;top:50px;width:120px;gap:5px"><span class="badge navy" style="width:11px;height:11px;color:#fff;font-size:5px">2</span><div><div class="h">Your Text Here</div><p class="p">Short note.</p></div></div>
  <div class="abs row" style="left:258px;top:120px;width:120px;gap:5px"><span class="badge sage" style="width:11px;height:11px;color:#fff;font-size:5px">4</span><div><div class="h">Your Text Here</div><p class="p">Short note.</p></div></div>
  <div class="foot"><span>Tolvane Consulting · Presentation Title</span><span class="fmark"></span></div>
</section>

<!-- 38 Price -->
<section class="slide">
  <div class="title">Price Slide</div>
  <div class="abs row" style="left:12px;right:12px;top:34px;gap:5px">
    <div style="flex:1;border:1px solid var(--line)"><div class="sage" style="height:12px"></div><div style="text-align:center;font-size:10px;font-weight:300;padding:10px 0">$99</div><p class="p" style="text-align:center;padding-bottom:10px">One<br>Two<br>Three</p><div class="char" style="height:8px"></div></div>
    <div style="flex:1;border:1px solid var(--line)"><div class="navy" style="height:12px"></div><div style="text-align:center;font-size:10px;font-weight:300;padding:10px 0">$199</div><p class="p" style="text-align:center;padding-bottom:10px">One<br>Two<br>Three</p><div class="char" style="height:8px"></div></div>
    <div style="flex:1;border:1px solid var(--line)"><div class="navy" style="height:12px"></div><div style="text-align:center;font-size:10px;font-weight:300;padding:10px 0">$299</div><p class="p" style="text-align:center;padding-bottom:10px">One<br>Two<br>Three</p><div class="char" style="height:8px"></div></div>
    <div style="flex:1;border:1px solid var(--line)"><div class="navy" style="height:12px"></div><div style="text-align:center;font-size:10px;font-weight:300;padding:10px 0">$399</div><p class="p" style="text-align:center;padding-bottom:10px">One<br>Two<br>Three</p><div class="char" style="height:8px"></div></div>
    <div style="flex:1;border:1px solid var(--line)"><div class="tan" style="height:12px"></div><div style="text-align:center;font-size:10px;font-weight:300;padding:10px 0">$499</div><p class="p" style="text-align:center;padding-bottom:10px">One<br>Two<br>Three</p><div class="tan" style="height:8px"></div></div>
  </div>
  <div class="foot"><span>Tolvane Consulting · Presentation Title</span><span class="fmark"></span></div>
</section>

<!-- 39 Who we are -->
<section class="slide">
  <div class="title">Who We Are?</div>
  <div class="abs" style="left:12px;right:12px;top:36px">
    <div class="row" style="gap:16px;border-bottom:1px solid var(--line);padding:8px 0"><div style="width:80px;font-size:7px;font-weight:300;color:var(--tan)">A Title About Us</div><p class="p" style="flex:1">Short paragraph that explains who we are and what we do.</p></div>
    <div class="row" style="gap:16px;border-bottom:1px solid var(--line);padding:8px 0"><div style="width:80px;font-size:7px;font-weight:300;color:var(--tan)">A Title About Our Goals</div><p class="p" style="flex:1">Short paragraph that explains our goals for our clients.</p></div>
    <div class="row" style="gap:16px;padding:8px 0"><div style="width:80px;font-size:7px;font-weight:300;color:var(--tan)">A Title About Services</div><p class="p" style="flex:1">Short paragraph that lists our core services in brief.</p></div>
  </div>
  <div class="foot"><span>Tolvane Consulting · Presentation Title</span><span class="fmark"></span></div>
</section>

<!-- 40 Three steps -->
<section class="slide">
  <div class="title">Three Steps</div>
  <div class="abs" style="left:12px;top:38px;width:120px">
    <div class="row" style="gap:6px;margin-bottom:16px"><span class="badge tan" style="width:11px;height:11px;color:#fff"><svg class="ico"><use href="#i-search"/></svg></span><div><div class="h" style="color:var(--tan)">Sample Text</div><p class="p">Short note here.</p></div></div>
    <div class="row" style="gap:6px;margin-bottom:16px"><span class="badge sage" style="width:11px;height:11px;color:#fff"><svg class="ico"><use href="#i-gear"/></svg></span><div><div class="h">Sample Text</div><p class="p">Short note here.</p></div></div>
    <div class="row" style="gap:6px"><span class="badge navy" style="width:11px;height:11px;color:#fff"><svg class="ico"><use href="#i-star"/></svg></span><div><div class="h">Sample Text</div><p class="p">Short note here.</p></div></div>
  </div>
  <svg class="abs" style="left:200px;top:24px" width="160" height="180" viewBox="0 0 160 180"><g fill="none" stroke-width="18"><circle cx="95" cy="40" r="26" stroke="var(--tan)"/><circle cx="65" cy="95" r="26" stroke="var(--sage)"/><circle cx="95" cy="145" r="26" stroke="var(--navy)"/></g>
    <g fill="none" stroke-width="1.8" stroke-linecap="round" stroke-linejoin="round"><use href="#i-search" x="86" y="31" width="18" height="18" stroke="var(--tan)"/><use href="#i-gear" x="56" y="86" width="18" height="18" stroke="var(--sage)"/><use href="#i-star" x="86" y="136" width="18" height="18" stroke="var(--navy)"/></g></svg>
  <div class="foot"><span>Tolvane Consulting · Presentation Title</span><span class="fmark"></span></div>
</section>

<!-- 41 Timeline -->
<section class="slide">
  <div class="title">Project Timeline</div>
  <svg class="abs" style="left:12px;top:30px" width="370" height="160" viewBox="0 0 370 160">
    <g fill="var(--mute)" font-size="4" font-family="Raleway, sans-serif"><text x="70" y="6">Jan</text><text x="95" y="6">Feb</text><text x="120" y="6">Mar</text><text x="145" y="6">Apr</text><text x="170" y="6">May</text><text x="195" y="6">Jun</text><text x="220" y="6">Jul</text><text x="245" y="6">Aug</text><text x="270" y="6">Sep</text><text x="295" y="6">Oct</text><text x="320" y="6">Nov</text><text x="345" y="6">Dec</text></g>
    <g stroke="var(--line)" stroke-width=".5"><line x1="0" y1="18" x2="370" y2="18"/><line x1="0" y1="34" x2="370" y2="34"/><line x1="0" y1="50" x2="370" y2="50"/><line x1="0" y1="66" x2="370" y2="66"/><line x1="0" y1="82" x2="370" y2="82"/><line x1="0" y1="98" x2="370" y2="98"/><line x1="0" y1="114" x2="370" y2="114"/><line x1="0" y1="130" x2="370" y2="130"/></g>
    <g fill="var(--ink)" font-size="4.5" font-family="Raleway, sans-serif"><text x="0" y="15">Research</text><text x="0" y="31">Planning</text><text x="0" y="47">Design</text><text x="0" y="63">Review</text><text x="0" y="79">Build</text><text x="0" y="95">Testing</text><text x="0" y="111">Launch</text><text x="0" y="127">Report</text></g>
    <rect x="70" y="10" width="290" height="5" fill="var(--tan)"/>
    <rect x="90" y="26" width="120" height="5" fill="var(--navy)"/>
    <rect x="140" y="42" width="100" height="5" fill="var(--sage)"/>
    <rect x="160" y="58" width="150" height="5" fill="var(--tan)"/>
    <rect x="120" y="74" width="90" height="5" fill="var(--navy)"/>
    <rect x="200" y="90" width="110" height="5" fill="var(--sage)"/>
    <rect x="230" y="106" width="80" height="5" fill="var(--tan)"/>
    <rect x="280" y="122" width="70" height="5" fill="var(--navy)"/>
    <g font-size="4" fill="var(--mute)" font-family="Raleway, sans-serif"><circle cx="80" cy="148" r="2" fill="var(--tan)"/><text x="85" y="150">Phase one</text><circle cx="160" cy="148" r="2" fill="var(--navy)"/><text x="165" y="150">Phase two</text><circle cx="240" cy="148" r="2" fill="var(--sage)"/><text x="245" y="150">Phase three</text></g>
  </svg>
  <div class="foot"><span>Tolvane Consulting · Presentation Title</span><span class="fmark"></span></div>
</section>

<!-- 42 Thank you -->
<section class="slide">
  <svg class="abs" width="394" height="220" viewBox="0 0 394 220"><polygon points="0,0 394,0 394,150 310,220 0,220" fill="var(--navy)"/></svg>
  <div class="abs" style="left:14px;top:12px;font-size:17px;font-weight:300;color:#fff;letter-spacing:.5px">THANK YOU</div>
  <div class="abs h" style="left:14px;top:36px;color:#fff">Presenter Name</div>
  <p class="p abs" style="left:14px;top:46px;width:200px;color:var(--soft)">Add a closing note, report details or next steps for the client in a few short lines here.</p>
  <div class="abs sub" style="left:14px;top:150px;color:var(--soft)">Contact Details</div>
  <div class="abs row" style="left:14px;top:161px;gap:4px;align-items:center;color:#fff"><svg class="ico" style="width:7px;height:7px"><use href="#i-phone"/></svg><span class="p" style="color:var(--soft)">+00 000 000 000</span></div>
  <div class="abs row" style="left:14px;top:171px;gap:4px;align-items:center;color:#fff"><svg class="ico" style="width:7px;height:7px"><use href="#i-mail"/></svg><span class="p" style="color:var(--soft)">hello@tolvane.example</span></div>
  <div class="brand" style="right:12px;bottom:6px"><span class="mark" style="width:8px;height:8px"></span><span class="name" style="font-size:4px">Tolvane Consulting</span></div>
</section>

</main>
</body>
</html>
```